Australian Wine export company Need a Wine label design

We need a wine label design for a new branded Australian wine based in South Australia called " HALLORAN " .
We will use this brand name ' HALLORAN' to marketing Australian Red wine and White wine into Chinese Market.
We would like to see the label designs that look classic and make consumers feel this is a superior quality Australian wine.
This label is to promote AUSTRALIAN WINE, need wine related and country related theme, need to give the consumer first impression that this wine is from AUSTRALIA.

Thanks
Updates

The following information are required to be presented on the wine label:

1) Brand Name: Halloran
2) Logo
3) Year of Vintage
4) Varietal
5) Place of production: South Australia
6) Fine Wine of Australia

Thanks.

Target Market(s)

Chinese market

Industry/Entity Type

Marketing

Requirements
Must have
• Need label design and renderings on the bottles.
Nice to have
• Label make consumers feel this is a superior quality Australian Wine.

```html
<!DOCTYPE html>
<html lang="en">
<head>
<meta charset="utf-8">
<title>Halloran Chardonnay Label</title>
<link rel="stylesheet" href="https://fonts.googleapis.com/css2?family=Alegreya:wght@400;500&display=swap">
<style>
  :root {
    --page: #f6f1e6;
    --gold-light: #f6e39a;
    --gold: #d4aa3c;
    --gold-dark: #8a6414;
    --green-deep: #0f3f1c;
    --green: #1d6a2c;
    --green-light: #3f8f3d;
    --cream-text: #f4f1e2;
    --ribbon-text: #3b2a07;
  }
  html, body {
    margin: 0;
    padding: 0;
    width: 960px;
    height: 1200px;
    overflow: hidden;
    background: var(--page);
  }
  .label-canvas {
    display: block;
    width: 960px;
    height: 1200px;
  }
  .label-text {
    font-family: "Alegreya", Georgia, serif;
    text-anchor: middle;
  }
  .brand-name { fill: var(--gold-light); font-size: 64px; }
  .ribbon-line { fill: var(--ribbon-text); font-size: 30px; }
  .varietal { fill: var(--cream-text); font-size: 92px; }
  .region { fill: var(--cream-text); font-size: 42px; }
  .vintage { fill: var(--cream-text); font-size: 40px; }
  .fine-print { fill: var(--cream-text); font-size: 19px; }
</style>
</head>
<body>
<svg class="label-canvas" viewBox="0 0 960 1200" xmlns="http://www.w3.org/2000/svg">
  <defs>
    <linearGradient id="gold-frame" x1="0" y1="0" x2="1" y2="1">
      <stop offset="0" stop-color="var(--gold-light)"/>
      <stop offset="0.35" stop-color="var(--gold)"/>
      <stop offset="0.65" stop-color="var(--gold-light)"/>
      <stop offset="1" stop-color="var(--gold-dark)"/>
    </linearGradient>
    <linearGradient id="gold-ribbon" x1="0" y1="0" x2="0" y2="1">
      <stop offset="0" stop-color="var(--gold-light)"/>
      <stop offset="0.5" stop-color="var(--gold)"/>
      <stop offset="1" stop-color="var(--gold-dark)"/>
    </linearGradient>
    <radialGradient id="vineyard-tones" cx="0.5" cy="0.35" r="0.8">
      <stop offset="0" stop-color="var(--green-light)"/>
      <stop offset="0.55" stop-color="var(--green)"/>
      <stop offset="1" stop-color="var(--green-deep)"/>
    </radialGradient>
    <radialGradient id="seal-green" cx="0.5" cy="0.4" r="0.6">
      <stop offset="0" stop-color="var(--green-light)"/>
      <stop offset="1" stop-color="var(--green-deep)"/>
    </radialGradient>
  </defs>

  <!-- main label panel -->
  <g class="label-panel">
    <rect class="panel-frame" x="200" y="470" width="560" height="620" rx="26" fill="url(#gold-frame)"/>
    <rect class="panel-inner-line" x="214" y="484" width="532" height="592" rx="18" fill="var(--gold-dark)"/>
    <rect class="panel-vineyard" x="220" y="490" width="520" height="580" rx="14"
          fill="url(#vineyard-tones)" role="img" aria-label="Photograph of vineyard rows on rolling green hills"/>
  </g>

  <!-- brand seal -->
  <g class="brand-seal">
    <circle cx="480" cy="400" r="182" fill="url(#gold-frame)"/>
    <circle cx="480" cy="400" r="166" fill="url(#seal-green)"/>
    <text class="label-text brand-name" x="480" y="380">Halloran</text>
  </g>

  <!-- ribbon -->
  <g class="tagline-ribbon">
    <polygon points="176,480 226,480 226,540 176,540 196,510" fill="var(--gold-dark)"/>
    <polygon points="784,480 734,480 734,540 784,540 764,510" fill="var(--gold-dark)"/>
    <rect x="212" y="464" width="536" height="66" fill="url(#gold-ribbon)"/>
    <text class="label-text ribbon-line" x="480" y="508">Fine Wine of Australia</text>
  </g>

  <!-- wine details -->
  <g class="wine-details">
    <text class="label-text varietal" x="480" y="690">Chardonnay</text>
    <text class="label-text region" x="480" y="860">South Australia</text>
    <text class="label-text vintage" x="480" y="912">2007</text>
    <text class="label-text fine-print" x="248" y="1040" style="text-anchor:start">ALC 13.5% by Vol.</text>
    <text class="label-text fine-print" x="712" y="1040" style="text-anchor:end">750 ml</text>
  </g>
</svg>
</body>
</html>
```